QBoost480 Business Card Design

I am in need of a business card design.

Business Name: Quantum Boost 480 or Qboost480 (we can try the business card with both variations)

I would like it to be somewhat different from the "average" business card

What do we do?

We link up with distributors of different items and we Market their products, sell their products, fulfill the shipment, and handle all customer service that goes along with it.

I will be uploading our logo as well as other business card ideas that i have seen and liked on the web.

I like the style of the "graphic design" business card that i uploaded. I was thinking maybe something like that but instead would read.

LINK | SELL | SEND

With maybe:
a computer or a Sync icon underneath SYNC
Some form of money sign underneath Sell
a delivery truck or something underneath SHIP.

And then I was thinking maybe put the logo on the back side like in the other business card that i uploaded.

I definitely want a double sided business card.

These are only my suggestions and if i was very confident in my idea then I wouldn't have to be on here. (So make what you think is nice because my opinion is probably not so great anyway!!)

Everything can be changed.

ALSO, For the logo
We can try and remove the text multi channel selling

For the Business card contact info:
Milo Quenton
CEO
2914 Ravensby Street
J7T-2K8
Kingsford, Ontario

Thanks

Target Market(s)

Businesses

Industry/Entity Type

Information Technology

Font styles to use
Serif
Sans Serif
Decorative

Colors
34a6d6
33b8a4
aaaaaa
85cae6
33a6d7
0492cd
9d9d9d

Requirements
Must have
• Double Sided Business card
Nice to have
• Illustration graphics / Icons underneath the main points

```html
<!DOCTYPE html>
<html lang="en">
<head>
<meta charset="utf-8">
<title>QBoost480 Business Card</title>
<link rel="stylesheet" href="https://fonts.googleapis.com/css2?family=Lato:wght@400;700;900&display=swap">
<style>
  :root {
    --backdrop: #2b2b2b;
    --card: #f7f7f7;
    --brand-blue: #0492cd;
    --sky-blue: #34a6d6;
    --leaf-green: #7dbb35;
    --slate: #5f5f5f;
    --white: #ffffff;
  }
  html, body {
    margin: 0;
    width: 1200px;
    height: 997px;
    overflow: hidden;
    background: var(--backdrop);
    font-family: "Lato", sans-serif;
  }
  .stage {
    position: relative;
    width: 1200px;
    height: 997px;
  }
  .card {
    position: absolute;
    top: 348px;
    width: 520px;
    height: 300px;
    border-radius: 22px;
    background: var(--card);
    overflow: hidden;
  }
  .card--back { left: 70px; }
  .card--front { left: 610px; }
  .card svg.swoosh {
    position: absolute;
    inset: 0;
    width: 520px;
    height: 300px;
  }
  .swoosh .band { fill: var(--brand-blue); }
  .swoosh .accent { fill: none; stroke: var(--leaf-green); stroke-width: 7; }

  /* back side */
  .pillars {
    position: absolute;
    left: 30px;
    top: 70px;
    margin: 0;
    font-weight: 400;
    font-size: 34px;
    letter-spacing: 2px;
    color: var(--sky-blue);
  }
  .pillar-icons {
    position: absolute;
    left: 30px;
    top: 128px;
    width: 300px;
    height: 60px;
  }
  .pillar-icons .icon { fill: var(--leaf-green); stroke: var(--leaf-green); }
  .brand-name {
    position: absolute;
    margin: 0;
    font-weight: 700;
    display: flex;
    align-items: center;
    gap: 8px;
  }
  .brand-name .dot {
    width: 12px;
    height: 12px;
    border-radius: 2px;
    background: currentColor;
  }
  .card--back .brand-name {
    right: 28px;
    bottom: 34px;
    font-size: 32px;
    color: var(--white);
  }

  /* front side */
  .card--front .brand-name {
    right: 28px;
    top: 42px;
    font-size: 38px;
    color: var(--slate);
  }
  .holder {
    position: absolute;
    left: 34px;
    top: 100px;
  }
  .holder-name {
    margin: 0;
    font-weight: 700;
    font-size: 19px;
    color: var(--leaf-green);
  }
  .holder-role {
    margin: 2px 0 0 6px;
    font-size: 11px;
    color: var(--sky-blue);
  }
  .contact {
    position: absolute;
    left: 30px;
    top: 218px;
    margin: 0;
    padding: 0;
    list-style: none;
    color: var(--white);
    font-size: 13px;
    line-height: 1.3;
  }
  .contact li {
    display: flex;
    align-items: flex-start;
    gap: 12px;
    margin-bottom: 4px;
  }
  .contact svg { width: 12px; height: 14px; flex: none; margin-top: 1px; fill: var(--white); }
</style>
</head>
<body>
<main class="stage">

  <section class="card card--back" aria-label="Card back">
    <svg class="swoosh" viewBox="0 0 520 300" aria-hidden="true">
      <path class="band" d="M230 300 Q330 130 520 58 L520 300 Z"/>
      <path class="accent" d="M218 300 Q320 110 520 40"/>
    </svg>
    <h2 class="pillars">LINK | SELL | SEND</h2>
    <svg class="pillar-icons" viewBox="0 0 300 60" aria-hidden="true">
      <g class="icon" fill="none" stroke-width="5">
        <path d="M26 14 A18 18 0 0 1 50 24" />
        <path d="M50 42 A18 18 0 0 1 26 48" />
        <path d="M14 38 A18 18 0 0 1 18 18" />
      </g>
      <g class="icon" stroke="none">
        <path d="M46 18 L56 26 L44 30 Z"/>
        <path d="M30 54 L20 46 L32 42 Z"/>
        <path d="M10 32 L16 42 L22 32 Z"/>
      </g>
      <text x="138" y="46" class="icon" stroke="none" font-family="Lato, sans-serif" font-weight="900" font-size="44">$</text>
      <g class="icon" stroke="none">
        <rect x="225" y="8" width="48" height="30" rx="2"/>
        <path d="M205 38 L205 24 L212 16 L223 16 L223 38 Z"/>
        <circle cx="214" cy="42" r="6"/>
        <circle cx="260" cy="42" r="6"/>
      </g>
    </svg>
    <h1 class="brand-name"><span class="dot"></span>Qboost480</h1>
  </section>

  <section class="card card--front" aria-label="Card front">
    <svg class="swoosh" viewBox="0 0 520 300" aria-hidden="true">
      <path class="band" d="M0 208 Q250 120 520 178 L520 300 L0 300 Z"/>
      <path class="accent" d="M0 196 Q230 110 460 150"/>
    </svg>
    <h1 class="brand-name"><span class="dot"></span>Qboost480</h1>
    <div class="holder">
      <p class="holder-name">Milo Quenton</p>
      <p class="holder-role">C.E.O</p>
    </div>
    <ul class="contact">
      <li>
        <svg viewBox="0 0 12 14" aria-hidden="true"><path d="M2 0 H10 A2 2 0 0 1 12 2 V12 A2 2 0 0 1 10 14 H2 A2 2 0 0 1 0 12 V2 A2 2 0 0 1 2 0 Z M2 2 V10 H10 V2 Z"/></svg>
        <span>514-2270-3968</span>
      </li>
      <li>
        <svg viewBox="0 0 12 14" aria-hidden="true"><path d="M0 3 H12 V11 H0 Z M1 4 L6 8 L11 4 Z" fill-rule="evenodd"/></svg>
        <span>hello@qboost480.com</span>
      </li>
      <li>
        <svg viewBox="0 0 12 14" aria-hidden="true"><path d="M6 0 A5 5 0 0 1 11 5 C11 9 6 14 6 14 C6 14 1 9 1 5 A5 5 0 0 1 6 0 Z M6 3 A2 2 0 1 0 6 7 A2 2 0 1 0 6 3 Z" fill-rule="evenodd"/></svg>
        <span>2914 Ravensby Street J7T-2K8<br>Kingsford, Ontario</span>
      </li>
    </ul>
  </section>

</main>
</body>
</html>
```